Web Site for Strategy and Technology Consulting Company

We are looking for a website design that engages potential customers to understand our services and contact us. In this contest, we are looking for a homepage design, but the winning designer will be favored for the design of some of the more complicated interior pages of the site. An additional contest (or contests) for these pages will be added soon.

PLATROM AND RESPONSIVE DESIGN
The site will be implemented in WordPress using the Elementor page builder.
We are looking for a design that will look good on phones are well as laptop browsers.

UPLOADED FILES INCLUDE:
1a A wireframe of the homepage we are looking for. The Uploaded PDF also includes a draft of the text proposed for the homepage. Designers are free to go beyond the wireframe, but all elements of the wireframe should be included.
1b A Word document with the draft text of the homepage.
2a-d The Corvalin logo. Two versions are included – a dark version which works well against a light background, and a light version which works well against a dark background.
3 The Corvalin color palette with HEX and RGB values. Designers are not limited to this palette, but colors should be complementary.
4 A draft of the homepage menu
5 Service sheets with information on the services we provide

MORE ABOUT CORVALIN
Corvalin is a consulting company focused on transforming businesses through software. Our tagline, “Transformation Delivered,” recognizes the gap business often have between business transformation and the software they end up with. By listening to our customers and understanding their vision and where they are, we help get our customers where they want to go.

We increase our capability by working with many consultants and partners, allowing us to provide our customers with the best people and the software that best suits them.

Industry/Entity Type

Consulting

Number of Pages Required

1 page

Font styles to use
Sans Serif

Requirements
Must have
• the content represented on the wireframe uploaded
Nice to have
• interactive features, such as roll-over icons that reveal additional information

```html
<!DOCTYPE html>
<html lang="en">
<head>
<meta charset="utf-8">
<title>Corvalin — Transformation Delivered</title>
<link href="https://fonts.googleapis.com/css2?family=Oxanium:wght@500;600;700&family=Lato:wght@400;700&display=swap" rel="stylesheet">
<style>
:root{
  --blue:#23609a;
  --blue-deep:#1d5188;
  --navy:#0f1c34;
  --yellow:#e2b80f;
  --ink:#222a33;
  --muted:#4a4f57;
  --soft-blue:#bcdcf0;
  --grey-bg:#f1f2f4;
  --white:#ffffff;
}
*{box-sizing:border-box;margin:0;padding:0}
html,body{width:1200px;height:3435px;overflow:hidden;background:var(--white)}
body{position:relative;font-family:'Lato',sans-serif;color:var(--ink)}
.abs{position:absolute}
.display{font-family:'Oxanium',sans-serif;font-weight:600}
.btn{position:absolute;background:var(--yellow);color:var(--navy);font-size:15px;border-radius:6px;display:flex;align-items:center;justify-content:center}
.wordmark{font-family:'Lato',sans-serif;font-weight:400;font-size:38px;letter-spacing:0.5px}

.site-header{position:absolute;left:0;top:0;width:1200px;height:114px;background:var(--white)}
.site-header .wordmark{position:absolute;left:110px;top:32px;color:#4d5560}
.nav a{position:absolute;top:47px;font-size:15px;color:var(--ink);text-decoration:none}

.hero{position:absolute;left:0;top:114px;width:1200px;height:633px;overflow:hidden}
.hero-bg{position:absolute;left:0;top:0;width:1200px;height:622px;background:radial-gradient(ellipse at 72% 55%,#3d5d8a 0%,#1f3558 35%,#101d36 75%)}
.hero-band{position:absolute;left:0;top:622px;width:1200px;height:11px;background:var(--yellow)}
.hero h1{position:absolute;left:0;top:112px;width:1200px;text-align:center;font-size:35px;color:var(--white);font-weight:600}
.hero .lead{position:absolute;left:150px;top:184px;width:900px;text-align:center;font-size:17px;line-height:29.5px;color:#eef2f7}
.ticks{position:absolute;left:220px;top:305px;list-style:none;color:#eef2f7;font-size:17px;line-height:29.3px}
.ticks li{position:relative;padding-left:27px}
.ticks li::before{content:"";position:absolute;left:2px;top:11px;width:8px;height:8px;border-radius:50%;background:currentColor}
.hero .closing{position:absolute;left:0;top:437px;width:1200px;text-align:center;font-weight:700;font-size:17px;color:var(--white)}

.section-title{position:absolute;left:0;width:1200px;text-align:center;color:var(--blue);font-size:37px}
.intro{position:absolute;left:113px;top:916px;width:980px;font-size:17px;line-height:29.3px;color:var(--muted)}
.diff-box{position:absolute;left:113px;top:1044px;width:975px;height:109px;background:var(--blue);border-radius:14px}
.diff-box h2{position:absolute;left:50px;top:40px;color:var(--white);font-size:24px;font-weight:700}
.service{position:absolute;top:1220px;width:200px;text-align:center}
.service h3{font-family:'Oxanium',sans-serif;font-weight:600;font-size:19px;line-height:29px;color:var(--ink);height:100px;display:flex;align-items:flex-end;justify-content:center;padding-bottom:14px}
.service .icon{width:96px;height:96px;border-radius:50%;background:var(--soft-blue);margin:0 auto;display:flex;align-items:center;justify-content:center}
.service .icon-name{font-size:17px;color:var(--ink)}
.service p{margin-top:14px;font-size:16px;line-height:26px;color:var(--muted)}
.find-out{position:absolute;left:0;top:1615px;width:1200px;text-align:center;font-size:17px;color:var(--muted)}

.resources{position:absolute;left:0;top:1709px;width:1200px;height:473px;background:var(--blue);color:var(--white)}
.resources h2{position:absolute;left:114px;top:56px;font-size:36px}
.resources h3{position:absolute;left:114px;top:108px;font-size:24px}
.resources .body{position:absolute;left:114px;top:167px;width:980px;font-size:17px;line-height:29px}
.resources .ticks{left:114px;top:250px}
.resources .wrap-up{position:absolute;left:112px;top:326px;font-size:17px}

.card{position:absolute;top:2372px;width:352px;height:190px;border:1.5px solid #9db4d3;border-radius:6px;background:var(--white)}
.card .avatar{position:absolute;left:18px;top:18px;width:50px;height:50px;border-radius:50%;background:linear-gradient(135deg,#8d7a6a,#4b433e)}
.card .name{position:absolute;left:80px;top:24px;font-size:17px;color:var(--ink)}
.card .stars{position:absolute;left:80px;top:47px}
.card p{position:absolute;left:18px;top:87px;width:316px;font-size:15px;line-height:29px;color:var(--muted);text-align:justify}

.tech{position:absolute;left:0;top:2731px;width:1200px;height:380px;background:var(--grey-bg)}
.tech h2{position:absolute;left:0;top:40px;width:1200px;text-align:center;font-size:37px;color:var(--blue)}
.tech .sub{position:absolute;left:0;top:98px;width:1200px;text-align:center;font-size:17px;color:var(--ink)}
.partner{position:absolute;top:222px;width:220px;text-align:center;font-size:28px;color:#3a4f6e;font-weight:700}
.arrow{position:absolute;top:211px;width:32px;height:32px;border-radius:50%;background:var(--blue-deep);display:flex;align-items:center;justify-content:center}

.footer{position:absolute;left:0;top:3111px;width:1200px;height:259px;background:linear-gradient(100deg,#16243f 0%,#0d1527 100%);overflow:hidden}
.footer-band{position:absolute;left:0;top:0;width:1200px;height:11px;background:var(--yellow)}
.footer .wordmark{position:absolute;left:118px;top:138px;color:var(--white);font-size:42px}
.links{position:absolute;top:56px;list-style:none;color:var(--white);font-size:15px;line-height:29px}
.links li:first-child{font-size:18px;font-weight:700}
.email{position:absolute;left:787px;top:55px;width:304px;height:49px;background:var(--white);border-radius:6px}
.email span{position:absolute;left:20px;top:15px;font-size:16px;color:#9aa0a8}
.footer .note{position:absolute;left:790px;top:124px;width:300px;font-size:17px;line-height:29px;color:var(--white)}
.copyright{position:absolute;left:0;top:3370px;width:1200px;height:65px;background:var(--blue);color:var(--white);font-size:17px;text-align:center;line-height:65px}
</style>
</head>
<body>

<header class="site-header">
  <div class="wordmark">Corvalin</div>
  <nav class="nav">
    <a style="left:433px">About Us</a>
    <a style="left:541px">Services</a>
    <a style="left:643px">Insights</a>
    <a style="left:743px">Join Us</a>
  </nav>
  <a class="btn" style="left:949px;top:36px;width:139px;height:43px">Contact Us</a>
</header>

<section class="hero">
  <div class="hero-bg" role="img" aria-label="Dark blue photo of a hand touching a glowing digital network globe"></div>
  <div class="hero-band"></div>
  <h1 class="display">Transformation Delivered</h1>
  <p class="lead">We do more for our customers than implement software. We listen. We work to understand where they are in their transformation journey and where they want to go. We partner with them to clear the roadblocks that stand in their way, ensuring they reach their destination. At Corvalin, we:</p>
  <ul class="ticks">
    <li>Focus on business value, with an emphasis on delivering value quickly.</li>
    <li>Meet our customers where they are without backing them up to the beginning of their journey.</li>
    <li>Provide a wide range of services, from strategy to product support.</li>
    <li>Commit to our customer's long-term success.</li>
  </ul>
  <p class="closing">Corvalin is business transformation, delivered.</p>
  <a class="btn" style="left:531px;top:489px;width:139px;height:41px">Our Story</a>
</section>

<h2 class="section-title display" style="top:842px">Transformation Supported by Technology</h2>
<p class="intro">During our early years, Corvalin focused only on business transformation. We came to realize that successful transformation often depended on quality software implementations, and often more than one. Now we focus on five things, the five things most businesses need to reach their goals.</p>

<div class="diff-box">
  <h2>Differentiators around our services</h2>
  <a class="btn" style="left:783px;top:33px;width:139px;height:42px">How We Work</a>
</div>

<div class="service" style="left:91px">
  <h3>Business<br>Transformation</h3>
  <div class="icon"><svg width="52" height="46" viewBox="0 0 52 46" fill="none" stroke="#2a3f5e" stroke-width="2"><rect x="3" y="3" width="46" height="30"/><line x1="26" y1="33" x2="26" y2="42"/><line x1="16" y1="43" x2="36" y2="43"/><rect x="10" y="20" width="5" height="9"/><rect x="19" y="14" width="5" height="15"/><rect x="28" y="9" width="5" height="20"/></svg></div>
  <p>Define and execute<br>your strategy.</p>
</div>
<div class="service" style="left:297px">
  <h3>ERP<br>Implementations</h3>
  <div class="icon"><svg width="52" height="52" viewBox="0 0 52 52" fill="none" stroke="#2a3f5e" stroke-width="2"><circle cx="26" cy="26" r="20"/><circle cx="26" cy="26" r="11"/><circle cx="26" cy="26" r="5"/><path d="M26 4v6M26 42v6M4 26h6M42 26h6"/></svg></div>
  <p>Assess, upgrade, and<br>implement ERP<br>solutions to meet<br>your needs.</p>
</div>
<div class="service" style="left:504px">
  <h3>CRM<br>Implementations</h3>
  <div class="icon"><svg width="52" height="50" viewBox="0 0 52 50" fill="none" stroke="#2a3f5e" stroke-width="2"><rect x="4" y="16" width="30" height="30"/><rect x="10" y="24" width="8" height="8"/><rect x="10" y="36" width="18" height="4"/><circle cx="38" cy="14" r="8"/><circle cx="38" cy="14" r="3"/></svg></div>
  <p>Take your<br>relationships<br>to the next level.</p>
</div>
<div class="service" style="left:708px">
  <h3>BI and<br>Data</h3>
  <div class="icon"><svg width="52" height="50" viewBox="0 0 52 50" fill="none" stroke="#2a3f5e" stroke-width="2"><rect x="4" y="4" width="36" height="30"/><circle cx="32" cy="30" r="10"/><line x1="39" y1="37" x2="48" y2="46"/><line x1="10" y1="12" x2="28" y2="12"/><line x1="10" y1="19" x2="22" y2="19"/></svg></div>
  <p>Discover, connect,<br>and trust your<br>data.</p>
</div>
<div class="service" style="left:913px">
  <h3>Building the<br>Right Team of<br>People</h3>
  <div class="icon"><span class="icon-name">Elevate</span></div>
  <p>Hire resources for<br>your transformation<br>journey.</p>
</div>

<p class="find-out">Find out how Corvalin can help you put all the pieces together and get them done.</p>

<section class="resources">
  <h2 class="display">Resources</h2>
  <h3 class="display">It's the People</h3>
  <p class="body">The world has changed in the past twenty years. The people you need might not all work for one company. Our clients want the best resources, available quickly. That's why, in addition to our team of experts, we partner with:</p>
  <ul class="ticks">
    <li>A large network of expert consultants who are the best at what they do,</li>
    <li>Service providers all over the world to provide the resources and value that are right for you, available 24 x 7.</li>
  </ul>
  <p class="wrap-up">People are invariably at the center of our customer's success. Find out how we can add our experts to yours.</p>
  <a class="btn" style="left:544px;top:381px;width:112px;height:41px">Our Team</a>
</section>

<h2 class="section-title display" style="top:2278px">Testimonials</h2>

<svg width="0" height="0" style="position:absolute"><defs><symbol id="star" viewBox="0 0 10 10"><polygon points="5,0 6.2,3.6 10,3.7 7,6 8.1,9.7 5,7.5 1.9,9.7 3,6 0,3.7 3.8,3.6" fill="#23609a"/></symbol></defs></svg>

<div class="card" style="left:60px">
  <div class="avatar" role="img" aria-label="Portrait photo of the reviewer"></div>
  <div class="name">Daniel Ashford</div>
  <svg class="stars" width="68" height="11"><use href="#star" x="0" width="11" height="11"/><use href="#star" x="14" width="11" height="11"/><use href="#star" x="28" width="11" height="11"/><use href="#star" x="42" width="11" height="11"/><use href="#star" x="56" width="11" height="11"/></svg>
  <p>Lorem ipsum dolor sit amet, consectetur adipiscing elit, sed do eiusmod tempor incididunt ut labore magna aliqua.</p>
</div>
<div class="card" style="left:430px">
  <div class="avatar" role="img" aria-label="Portrait photo of the reviewer"></div>
  <div class="name">Daniel Ashford</div>
  <svg class="stars" width="68" height="11"><use href="#star" x="0" width="11" height="11"/><use href="#star" x="14" width="11" height="11"/><use href="#star" x="28" width="11" height="11"/><use href="#star" x="42" width="11" height="11"/><use href="#star" x="56" width="11" height="11"/></svg>
  <p>Lorem ipsum dolor sit amet, consectetur adipiscing elit, sed do eiusmod tempor incididunt ut labore magna aliqua.</p>
</div>
<div class="card" style="left:800px">
  <div class="avatar" role="img" aria-label="Portrait photo of the reviewer"></div>
  <div class="name">Daniel Ashford</div>
  <svg class="stars" width="68" height="11"><use href="#star" x="0" width="11" height="11"/><use href="#star" x="14" width="11" height="11"/><use href="#star" x="28" width="11" height="11"/><use href="#star" x="42" width="11" height="11"/><use href="#star" x="56" width="11" height="11"/></svg>
  <p>Lorem ipsum dolor sit amet, consectetur adipiscing elit, sed do eiusmod tempor incididunt ut labore magna aliqua.</p>
</div>

<a class="btn" style="left:544px;top:2613px;width:112px;height:41px">View More</a>

<section class="tech">
  <h2 class="display">Technologies</h2>
  <p class="sub">Rotator Of Technologies</p>
  <a class="arrow" style="left:36px"><svg width="12" height="14" viewBox="0 0 12 14"><polyline points="8,2 3,7 8,12" fill="none" stroke="#fff" stroke-width="2.2"/></svg></a>
  <div class="partner" style="left:100px">Meridian Suite</div>
  <div class="partner" style="left:345px">Stratus Cloud</div>
  <div class="partner" style="left:595px">Ledgerline</div>
  <div class="partner" style="left:878px">Halvora</div>
  <a class="arrow" style="left:1137px"><svg width="12" height="14" viewBox="0 0 12 14"><polyline points="4,2 9,7 4,12" fill="none" stroke="#fff" stroke-width="2.2"/></svg></a>
</section>

<footer class="footer">
  <div class="footer-band"></div>
  <div class="wordmark">Corvalin</div>
  <ul class="links" style="left:417px"><li>Quick Links</li><li>About Us</li><li>Services</li><li>Insights</li><li>Join Us</li></ul>
  <ul class="links" style="left:605px"><li>Help Links</li><li>Support</li><li>FAQ</li><li>Privacy Policy</li><li>Terms &amp; Conditions</li></ul>
  <div class="email"><span>Email</span>
    <svg class="abs" style="left:272px;top:16px" width="18" height="18" viewBox="0 0 18 18"><polygon points="1,1 17,9 1,17 4,9" fill="#2f7fe0"/></svg>
  </div>
  <p class="note">Lorem ipsum dolor sit amet, consectetur elit, sed do eiusmod.</p>
</footer>
<div class="copyright">© Copyrights 2023 Corvalin | All Rights Reserved</div>

</body>
</html>
```